Box Design for Flooring product

***IMPORTANT: PLEASE READ THE DOCUMENT PROVIDED WITH THIS BRIEF CAREFULLY BEFORE ACCEPTING THIS PROJECT***
Need a creative design for the packaging of a flooring product. The packaging is two boxes: one holding 36 planks of flooring, and the other 7 planks of flooring. There are 4 colours for the flooring planks that need a box designed (for both the 36 plank box and 7 plank box). The boxes measures 92 cm x 16cm x 7cm (36 planks) and 92 cm x 16cm x 1.5cm (7 planks).
More details are provided in the requirements document attached with this brief. Also attaching other supporting documents with this brief mentioned in the document.
Need extra days to review
- Montserrat-Regular

```html
<!DOCTYPE html>
<html lang="en">
<head>
<meta charset="utf-8">
<title>Solvenna Flooring Box</title>
<link href="https://fonts.googleapis.com/css2?family=Montserrat:wght@400;500;600&display=swap" rel="stylesheet">
<style>
  :root {
    --page: #f3f3f3;
    --box-dark: #2b2a27;
    --banner: #4a4336;
    --grain-light: #8a8a86;
    --grain-dark: #5c5c59;
    --text-light: #f2f2f0;
    --text-muted: #cfcfca;
    --accent-yellow: #e2b520;
    --badge: #e6e6e3;
    --badge-text: #3a3a38;
  }
  * { box-sizing: border-box; margin: 0; padding: 0; }
  html, body { width: 1200px; height: 1200px; overflow: hidden; }
  body {
    background: var(--page);
    font-family: "Montserrat", sans-serif;
    color: var(--text-light);
    position: relative;
  }
  .top-face {
    position: absolute;
    left: 40px; top: 380px;
    width: 1120px; height: 200px;
    background: var(--box-dark);
    display: flex;
    overflow: hidden;
  }
  .room-photo {
    width: 300px; height: 100%;
    background: linear-gradient(180deg, #e9e9e6 0%, #dcdcd8 55%, #8e8c86 56%, #6f6d68 100%);
    position: relative;
    flex-shrink: 0;
  }
  .yellow-band {
    position: absolute; right: 0; top: 0;
    width: 18px; height: 100%;
    background: var(--accent-yellow);
  }
  .wood-panel {
    position: relative;
    flex: 1;
    background: linear-gradient(90deg, var(--grain-dark), var(--grain-light) 30%, var(--grain-dark) 60%, var(--grain-light) 85%, var(--grain-dark));
  }
  .brand-banner {
    position: absolute; left: 0; top: 30px;
    width: 460px; height: 80px;
    background: var(--banner);
    border-radius: 0 40px 40px 0;
    display: flex; align-items: center; gap: 16px;
    padding-left: 40px;
  }
  .brand-mark {
    width: 36px; height: 36px;
    background: var(--text-light);
  }
  .brand-name {
    font-size: 40px; font-weight: 500; letter-spacing: 4px; line-height: 1;
  }
  .brand-tagline {
    font-size: 11px; letter-spacing: 3.5px; text-transform: uppercase; margin-top: 4px;
    color: var(--text-muted);
  }
  .info-strip {
    position: absolute; left: 0; bottom: 0;
    width: 100%; height: 78px;
    background: var(--box-dark);
    display: flex; align-items: center;
    padding: 0 24px;
  }
  .features {
    list-style: none;
    font-size: 12px; line-height: 16px;
    padding-left: 20px;
    border-left: 1px solid var(--text-muted);
    width: 300px;
  }
  .features li::before { content: "• "; }
  .specs {
    display: flex; gap: 26px;
    border-left: 1px solid var(--text-muted);
    padding-left: 22px;
  }
  .spec { display: flex; align-items: center; gap: 10px; font-size: 11px; line-height: 14px; }
  .spec-icon { width: 36px; height: 22px; }
  .badges {
    position: absolute; right: 24px; top: 18px;
    display: flex; gap: 14px;
  }
  .badge {
    width: 66px; height: 66px; border-radius: 50%;
    background: var(--badge); color: var(--badge-text);
    display: flex; align-items: center; justify-content: center;
    text-align: center; font-size: 8px; font-weight: 600; line-height: 10px;
    text-transform: uppercase; padding: 6px;
  }
  .end-face {
    position: absolute;
    left: 400px; top: 660px;
    width: 400px; height: 175px;
    background: var(--box-dark);
    display: flex; align-items: center; justify-content: center; gap: 18px;
  }
  .end-face .brand-name { font-size: 44px; }
</style>
</head>
<body>
  <section class="top-face">
    <div class="room-photo" role="img" aria-label="Bedroom with grey plank flooring, bed with red throw and a yellow side table">
      <div class="yellow-band"></div>
    </div>
    <div class="wood-panel" role="img" aria-label="Grey oak wood grain texture">
      <div class="brand-banner">
        <div class="brand-mark"></div>
        <div>
          <div class="brand-name">SOLVENNA</div>
          <div class="brand-tagline">Premium Floors and Tiles</div>
        </div>
      </div>
      <div class="badges">
        <div class="badge">Water Resistant</div>
        <div class="badge">Easy Clean</div>
        <div class="badge">Soft Feel</div>
      </div>
      <div class="info-strip">
        <ul class="features">
          <li>Easy to lay</li>
          <li>Water resistant, easy to clean</li>
          <li>Ideal for Bathrooms and Kitchens</li>
          <li>Suitable for general domestic use</li>
        </ul>
        <div class="specs">
          <div class="spec">
            <svg class="spec-icon" viewBox="0 0 36 22"><path d="M2 14 L22 4 L34 8 L14 18 Z" fill="#e6e6e3"/></svg>
            <span>Pack Size<br>7 Planks / 1m²</span>
          </div>
          <div class="spec">
            <svg class="spec-icon" viewBox="0 0 36 22"><rect x="3" y="4" width="30" height="14" fill="#e6e6e3"/></svg>
            <span>914 x 152mm<br>(36" x 6" approx.)</span>
          </div>
          <div class="spec">
            <svg class="spec-icon" viewBox="0 0 36 22"><path d="M2 12 L26 4 L34 6 L10 14 Z" fill="#e6e6e3"/></svg>
            <span>Thickness<br>1.8mm</span>
          </div>
        </div>
      </div>
    </div>
  </section>

  <section class="end-face">
    <div class="brand-mark"></div>
    <div>
      <div class="brand-name">SOLVENNA</div>
      <div class="brand-tagline">Premium Floors and Tiles</div>
    </div>
  </section>
</body>
</html>
```